Endocrinologist needs new stationery

I have a logo from MarkForge and now need stationery with the new logo.

Address: Suite 4, 282 Falcon Street, Richmond, VIC 3121
Phone: 03 9417 2253
Fax: 03 9417 2255
Website: www.drmaylacorwen.com.au
Email: admin@drmaylacorwen.com.au

```html
<!DOCTYPE html>
<html lang="en">
<head>
<meta charset="utf-8">
<title>Dr Mayla Corwen – Stationery Suite</title>
<link rel="stylesheet" href="https://fonts.googleapis.com/css2?family=Open+Sans:wght@400;600&display=swap">
<style>
:root{
  --navy:#2d4a7c;
  --mauve:#9a6f97;
  --backdrop:#e8e8e9;
  --paper:#f8f8f8;
  --ink:#2f2f33;
  --grid-tint:#f5f5f7;
  --white:#ffffff;
}
*{box-sizing:border-box;margin:0;padding:0}
html,body{width:1200px;height:801px;overflow:hidden}
body{background:var(--backdrop);font-family:"Open Sans",sans-serif;color:var(--ink);position:relative}
.sheet,.envelope,.notebook,.card{position:absolute;box-shadow:0 2px 6px rgba(0,0,0,.12)}
.brand-name{font-family:"Open Sans",sans-serif;font-weight:400;color:var(--navy);white-space:nowrap;letter-spacing:.2px}
.brand-name.on-dark{color:var(--white)}
.icon{width:7px;height:7px;fill:var(--navy);flex:none;margin-top:1px}

/* Blank letterhead */
.letterhead-blank{left:178px;top:28px;width:330px;height:467px;background:var(--paper)}
.letterhead-blank .brand-name{position:absolute;left:32px;top:44px;font-size:17px}
.writing-area{position:absolute;left:40px;top:100px;width:255px;height:285px;background:var(--grid-tint);border-radius:2px}
.footer-rule{position:absolute;left:30px;right:30px;top:398px;height:1px;background:var(--mauve)}
.contact-cols{position:absolute;left:32px;right:30px;top:410px;display:flex;justify-content:space-between;font-size:6.3px;line-height:1.45}
.contact-line{display:flex;gap:6px;align-items:flex-start;margin-bottom:4px}

/* Letter */
.letter{left:530px;top:22px;width:330px;height:467px;background:var(--paper);overflow:hidden}
.letter .brand-name{position:absolute;left:34px;top:44px;font-size:17px}
.letter-date{position:absolute;right:34px;top:103px;font-size:6.5px}
.addressee{position:absolute;left:40px;top:135px;font-size:6.5px;line-height:1.55}
.letter-body{position:absolute;left:40px;top:195px;width:232px;font-size:6.4px;line-height:1.65;text-align:justify}
.letter-body p{margin-bottom:9px}
.sign-off{position:absolute;left:40px;top:350px;font-size:6.4px}
.signature{position:absolute;left:40px;top:362px;width:90px;height:24px;background:linear-gradient(90deg,rgba(45,74,124,.14),rgba(45,74,124,.03))}
.sign-rule{position:absolute;left:40px;top:390px;width:70px;height:1px;background:var(--mauve)}
.signatory{position:absolute;left:40px;top:396px;font-size:6.5px;line-height:1.55;font-weight:600}
.letter-wave{position:absolute;left:0;bottom:0;width:330px;height:467px}

/* Notebook */
.notebook{left:895px;top:100px;width:200px;height:290px;background:var(--navy);border-radius:4px 10px 10px 4px}
.notebook .brand-name{position:absolute;left:20px;top:134px;font-size:15px}
.elastic-band{position:absolute;left:164px;top:0;width:9px;height:100%;background:var(--mauve)}

/* Envelopes */
.envelope{width:345px;height:225px}
.envelope-back{left:45px;top:515px;background:var(--navy);overflow:hidden}
.envelope-back .brand-name{position:absolute;left:80px;top:68px;font-size:18px}
.envelope-wave{position:absolute;inset:0;width:345px;height:225px}
.envelope-front{left:405px;top:515px;background:var(--paper)}
.envelope-front .brand-name{position:absolute;left:28px;top:34px;font-size:15px}
.return-address{position:absolute;left:230px;top:150px;padding-left:12px;border-left:1px solid var(--mauve);font-size:7px;line-height:1.7}

/* Business cards */
.card{left:780px;width:175px}
.card-front{top:515px;height:100px;background:var(--navy)}
.card-front .brand-name{position:absolute;left:0;right:0;top:40px;text-align:center;font-size:13px}
.card-back{top:625px;height:126px;background:var(--paper);padding:12px 0 0 18px}
.card-back .card-name{font-size:10px;line-height:1.3;color:var(--navy);font-weight:400}
.card-back .card-title{font-size:6px;line-height:1.3;color:var(--mauve);margin-bottom:8px}
.card-back .contact-line{font-size:5.8px;line-height:1.4;margin-bottom:4px;gap:7px}
.card-back .icon{width:6px;height:6px}
</style>
</head>
<body>

<svg width="0" height="0" style="position:absolute" aria-hidden="true">
  <symbol id="i-pin" viewBox="0 0 10 10"><path d="M5 0a3.5 3.5 0 0 0-3.5 3.5C1.5 6 5 10 5 10s3.5-4 3.5-6.5A3.5 3.5 0 0 0 5 0zm0 5a1.4 1.4 0 1 1 0-2.8A1.4 1.4 0 0 1 5 5z"/></symbol>
  <symbol id="i-phone" viewBox="0 0 10 10"><path d="M2 0.5l2 2-1 1.3c.6 1.3 1.6 2.3 2.9 2.9l1.3-1 2 2-1 1.8C4 9.5.5 6 .3 1.5z"/></symbol>
  <symbol id="i-fax" viewBox="0 0 10 10"><path d="M2.5 0h5v3h-5zM0.5 3.5h9v4.5h-2V6h-5v2h-2zM3 6.5h4V10H3z"/></symbol>
  <symbol id="i-web" viewBox="0 0 10 10"><path d="M5 0a5 5 0 1 0 0 10A5 5 0 0 0 5 0zm3.9 4.5H7.2A7 7 0 0 0 6.4 1a4 4 0 0 1 2.5 3.5zM5 1c.6.8 1.1 2 1.2 3.5H3.8C3.9 3 4.4 1.8 5 1zM3.6 1a7 7 0 0 0-.8 3.5H1.1A4 4 0 0 1 3.6 1zM1.1 5.5h1.7A7 7 0 0 0 3.6 9a4 4 0 0 1-2.5-3.5zM5 9c-.6-.8-1.1-2-1.2-3.5h2.4C6.1 7 5.6 8.2 5 9zm1.4 0a7 7 0 0 0 .8-3.5h1.7A4 4 0 0 1 6.4 9z"/></symbol>
  <symbol id="i-mail" viewBox="0 0 10 10"><path d="M0 2h10v.8L5 6 0 2.8zM0 3.9l5 3.2 5-3.2V8H0z"/></symbol>
</svg>

<section class="sheet letterhead-blank" aria-label="Letterhead, blank">
  <div class="brand-name">Dr Mayla Corwen</div>
  <div class="writing-area" role="img" aria-label="Very faint dot grid writing area"></div>
  <div class="footer-rule"></div>
  <div class="contact-cols">
    <div>
      <div class="contact-line"><svg class="icon"><use href="#i-pin"/></svg><span>Suite 4, 282 Falcon Street,<br>Richmond, VIC 3121</span></div>
      <div class="contact-line"><svg class="icon"><use href="#i-phone"/></svg><span>03 9417 2253</span></div>
      <div class="contact-line"><svg class="icon"><use href="#i-fax"/></svg><span>03 9417 2255</span></div>
    </div>
    <div>
      <div class="contact-line"><svg class="icon"><use href="#i-web"/></svg><span>www.drmaylacorwen.com.au</span></div>
      <div class="contact-line"><svg class="icon"><use href="#i-mail"/></svg><span>admin@drmaylacorwen.com.au</span></div>
    </div>
  </div>
</section>

<section class="sheet letter" aria-label="Letterhead with letter">
  <svg class="letter-wave" viewBox="0 0 330 467" aria-hidden="true">
    <path d="M60 467 C190 445 300 420 330 335 L330 467 Z" fill="var(--navy)"/>
    <path d="M60 467 C190 440 292 412 330 325" fill="none" stroke="var(--mauve)" stroke-width="4"/>
  </svg>
  <div class="brand-name">Dr Mayla Corwen</div>
  <div class="letter-date">20 May 2024</div>
  <div class="addressee">Ms. Clara Benning<br>48 Harlow Street<br>Melbourne VIC 3000</div>
  <div class="letter-body">
    <p>Dear Ms. Benning,</p>
    <p>Lorem ipsum dolor sit amet, consectetur adipiscing elit, sed do eiusmod tempor incididunt ut labore et dolore magna aliqua. Ut enim ad minim veniam, quis nostrud exercitation ullamco laboris nisi ut aliquip ex ea commodo consequat. Duis aute irure dolor in reprehenderit in voluptate velit esse cillum dolore eu fugiat nulla pariatur. Excepteur sint occaecat cupidatat non proident, sunt in culpa qui officia deserunt mollit anim id est laborum.</p>
    <p>Lorem ipsum dolor sit amet, consectetur adipiscing elit, sed do eiusmod tempor incididunt ut labore et dolore magna aliqua.</p>
  </div>
  <div class="sign-off">Kind regards,</div>
  <div class="signature" role="img" aria-label="Handwritten signature"></div>
  <div class="sign-rule"></div>
  <div class="signatory">Dr Mayla Corwen<br>Endocrinologist</div>
</section>

<section class="notebook" aria-label="Notebook cover">
  <div class="brand-name on-dark">Dr Mayla Corwen</div>
  <div class="elastic-band"></div>
</section>

<section class="envelope envelope-back" aria-label="Envelope, back">
  <svg class="envelope-wave" viewBox="0 0 345 225" aria-hidden="true">
    <path d="M140 225 C240 200 335 160 345 90" fill="none" stroke="var(--mauve)" stroke-width="4"/>
  </svg>
  <div class="brand-name on-dark">Dr Mayla Corwen</div>
</section>

<section class="envelope envelope-front" aria-label="Envelope, front">
  <div class="brand-name">Dr Mayla Corwen</div>
  <div class="return-address">Suite 4, 282 Falcon Street,<br>Richmond, VIC 3121</div>
</section>

<section class="card card-front" aria-label="Business card, front">
  <div class="brand-name on-dark">Dr Mayla Corwen</div>
</section>

<section class="card card-back" aria-label="Business card, back">
  <div class="card-name">Dr Mayla Corwen</div>
  <div class="card-title">Endocrinologist</div>
  <div class="contact-line"><svg class="icon"><use href="#i-pin"/></svg><span>Suite 4, 282 Falcon Street,<br>Richmond, VIC 3121</span></div>
  <div class="contact-line"><svg class="icon"><use href="#i-phone"/></svg><span>03 9417 2253</span></div>
  <div class="contact-line"><svg class="icon"><use href="#i-fax"/></svg><span>03 9417 2255</span></div>
  <div class="contact-line"><svg class="icon"><use href="#i-web"/></svg><span>www.drmaylacorwen.com.au</span></div>
  <div class="contact-line"><svg class="icon"><use href="#i-mail"/></svg><span>admin@drmaylacorwen.com.au</span></div>
</section>

</body>
</html>
```